Corporate Design für Hausverwalterin und Immobilienvermarktung
Zielgruppe
Hausverwalterin und Immobilienvermarktung
Aufgabenstellung
wir sind im Immobiliensektor unterwegs und das Design soll edel und hochwertig sein

```html
<!DOCTYPE html>
<html lang="de">
<head>
<meta charset="utf-8">
<title>Varnel Immobilien – Geschäftsausstattung</title>
<link href="https://fonts.googleapis.com/css2?family=Tinos&family=Poppins:wght@400&display=swap" rel="stylesheet">
<style>
:root{
  --navy:#13273f;
  --navy-deep:#11243a;
  --gold:#c0a05a;
  --gold-dark:#b08f4c;
  --gold-light:#e3ca85;
  --paper:#ffffff;
  --ink:#1d2433;
  --field:#e8e9eb;
  --grey-top:#7f8087;
  --grey-mid:#a9aaae;
}
*{margin:0;padding:0;box-sizing:border-box}
html,body{width:848px;height:1200px;overflow:hidden}
body{position:relative;background:linear-gradient(180deg,var(--grey-top) 313px,var(--grey-mid) 760px,#8e8f94 1200px);font-family:"Tinos",serif;color:var(--ink)}
.gold-bar{background:linear-gradient(90deg,var(--gold-dark),var(--gold) 30%,var(--gold-light) 55%,var(--gold) 80%,var(--gold-dark))}
.navy-bar{background:var(--navy)}
.brand{font-family:"Tinos",serif;font-weight:400;color:var(--gold);white-space:nowrap;display:flex;align-items:center;gap:.3em}
.brand .mark{display:inline-block;width:.5em;height:.5em;background:var(--gold)}

.hero{position:absolute;left:0;top:0;width:848px;height:313px;background:var(--navy);display:flex;align-items:center;justify-content:center}
.hero .brand{font-size:50px}

.sheet{position:absolute;background:var(--paper);overflow:hidden}
.letter{left:25px;top:375px;width:368px;height:514px}
.letter .gold-bar{height:12px}
.letter .navy-bar{position:absolute;left:0;bottom:0;width:100%;height:11px}
.letter .brand{font-size:14px;justify-content:center;margin-top:36px}
.letter-body{font-family:"Poppins",sans-serif;font-size:7px;letter-spacing:.85px;line-height:12.05px;text-align:center;color:var(--ink);width:300px;margin:28px auto 0}
.signature{position:absolute;left:248px;top:410px;width:66px;height:46px;background:linear-gradient(90deg,#f3f4f7,#eceef3)}

.contact{position:absolute;font-size:8px;line-height:11px;color:var(--ink)}
.contact li{list-style:none;display:flex;align-items:center;gap:4px}
.contact svg{width:7px;height:7px;flex:none}

.letter .contact{left:37px;top:459px}

.envelope .gold-bar{height:10px}
.envelope .navy-bar{position:absolute;left:0;bottom:0;width:100%;height:10px}
.env-front{left:433px;top:405px;width:372px;height:171px}
.env-front .brand{font-size:11px;position:absolute;left:10px;top:40px}
.window{position:absolute;left:8px;top:62px;width:119px;height:47px;border-radius:4px;background:var(--field)}
.env-front .contact{left:8px;top:118px}

.env-back{left:431px;top:646px;width:374px;height:178px}
.flap{position:absolute;left:0;top:0;width:100%;height:61px;background:var(--navy);border-radius:0 0 64px 64px/0 0 61px 61px;display:flex;justify-content:center;padding-top:10px}
.flap .brand{font-size:10px;transform:rotate(180deg);height:14px}
.env-back .brand.main{font-size:11px;position:absolute;left:10px;top:88px}
.env-back .contact{left:8px;top:126px}

.card{position:absolute;top:919px;width:381px;height:218px;background:var(--navy)}
.card-front{left:25px;display:flex;align-items:center;justify-content:center}
.card-front .brand{font-size:27px}
.card-back{left:441px;color:#f3f1ea;padding:25px 22px 0;text-transform:uppercase;font-size:8.6px;line-height:11px;letter-spacing:.1px}
.card-back h2{font-weight:400;font-size:10.8px;letter-spacing:.2px;margin-bottom:13px}
.card-back p{margin-bottom:13px}
.card-back ul{list-style:none;margin-bottom:10px;line-height:14.5px}
.card-back .contact{position:static;color:#f3f1ea;text-transform:none;display:flex;gap:9px;font-size:8.6px;margin-top:19px}
.card-back .contact li{gap:5px}
</style>
</head>
<body>
<svg width="0" height="0" style="position:absolute">
  <defs>
    <symbol id="icon-phone" viewBox="0 0 10 10"><path d="M2.2 .8l1.5 1.8-.9 1.1c.6 1.3 1.5 2.2 2.8 2.8l1.1-.9 1.8 1.5-.9 1.6C4.3 8.5 1.5 5.7.6 1.7z" fill="currentColor"/></symbol>
    <symbol id="icon-mail" viewBox="0 0 10 10"><rect x=".5" y="2" width="9" height="6.5" fill="currentColor"/><path d="M.8 2.4L5 5.6l4.2-3.2" stroke="#fff" stroke-width=".9" fill="none"/></symbol>
    <symbol id="icon-web" viewBox="0 0 10 10"><g fill="none" stroke="currentColor" stroke-width=".9"><circle cx="5" cy="5" r="4.2"/><ellipse cx="5" cy="5" rx="1.8" ry="4.2"/><path d="M.8 5h8.4M1.6 2.8h6.8M1.6 7.2h6.8"/></g></symbol>
  </defs>
</svg>

<header class="hero">
  <div class="brand"><span class="mark"></span>Varnel Immobilien</div>
</header>

<section class="sheet letter">
  <div class="gold-bar"></div>
  <div class="brand"><span class="mark"></span>Varnel Immobilien</div>
  <div class="letter-body">
    Lorem ipsum dolor sit amet, consectetuer adipiscing elit, sed diam nonummy nibh euismod tincidunt ut laoreet dolore magna aliquam erat volutpat. Ut wisi enim ad minim veniam, quis nostrud exerci tation ullamcorper suscipit lobortis nisl ut aliquip ex ea commodo consequat. Duis autem vel eum iriure dolor in hendrerit in vulputate velit esse molestie consequat, vel illum dolore eu feugiat nulla facilisis at vero eros et accumsan et iusto odio dignissim qui blandit praesent luptatum zzril delenit augue duis dolore te feugait nulla facilisi.<br>
    Lorem ipsum dolor sit amet, cons ectetuer adipiscing elit, sed diam nonummy nibh euismod tincidunt ut laoreet dolore magna aliquam erat volutpat. Ut wisi enim ad minim veniam, quis nostrud exerci tation ullamcorper suscipit lobortis nisl ut aliquip ex ea commodo consequat.<br>
    Lorem ipsum dolor sit amet, consectetuer adipiscing elit, sed diam nonummy nibh euismod tincidunt ut laoreet dolore magna aliquam erat volutpat. Ut wisi enim ad minim veniam, quis nostrud exerci tation ullamcorper suscipit lobortis nisl ut aliquip ex ea commodo consequat. Duis autem vel eum iriure dolor in hendrerit in vulputate velit esse molestie consequat, vel illum dolore eu feugiat nulla facilisis at vero eros et accumsan et iusto odio dignissim qui blandit praesent luptatum zzril delenit augue duis dolore te feugait nulla facilisi.
  </div>
  <div class="signature" role="img" aria-label="Handschriftliche Unterschrift"></div>
  <ul class="contact">
    <li><svg style="color:var(--gold)"><use href="#icon-phone"/></svg>0171 386 42 19</li>
    <li><svg style="color:var(--gold)"><use href="#icon-mail"/></svg>info@varnel-immobilien.de</li>
    <li><svg style="color:var(--gold)"><use href="#icon-web"/></svg>www.varnel-immobilien.de</li>
  </ul>
  <div class="navy-bar"></div>
</section>

<section class="sheet envelope env-front">
  <div class="gold-bar"></div>
  <div class="brand"><span class="mark"></span>Varnel Immobilien</div>
  <div class="window"></div>
  <ul class="contact">
    <li><svg style="color:var(--gold)"><use href="#icon-phone"/></svg>0171 386 42 19</li>
    <li><svg style="color:var(--gold)"><use href="#icon-mail"/></svg>info@varnel-immobilien.de</li>
    <li><svg style="color:var(--gold)"><use href="#icon-web"/></svg>www.varnel-immobilien.de</li>
  </ul>
  <div class="navy-bar"></div>
</section>

<section class="sheet envelope env-back">
  <div class="flap"><div class="brand"><span class="mark"></span>Varnel Immobilien</div></div>
  <div class="brand main"><span class="mark"></span>Varnel Immobilien</div>
  <ul class="contact">
    <li><svg style="color:var(--gold)"><use href="#icon-phone"/></svg>0171 386 42 19</li>
    <li><svg style="color:var(--gold)"><use href="#icon-mail"/></svg>info@varnel-immobilien.de</li>
    <li><svg style="color:var(--gold)"><use href="#icon-web"/></svg>www.varnel-immobilien.de</li>
  </ul>
  <div class="navy-bar"></div>
</section>

<section class="card card-front">
  <div class="brand"><span class="mark"></span>Varnel Immobilien</div>
</section>

<section class="card card-back">
  <h2>Ganzheitliche Immobilienbetreuung mit Strategie.</h2>
  <p>Als zertifizierte Hausverwalterin &amp; Immobilienmaklerin<br>gemäss § 34C GewO verbinde ich klassische Verwaltung<br>mit wertoptimierter Vermarktung:</p>
  <ul>
    <li>♦ Hausverwaltung: rechtssicher &amp; entlastend.</li>
    <li>♦ Asset Management: strategische Ertragssteigerung.</li>
    <li>♦ Verkauf: marktgerecht &amp; professionell.</li>
  </ul>
  <p>Varnel Immobilien - Ihr Eigentum in zuverlässigen Händen.</p>
  <ul class="contact">
    <li><svg><use href="#icon-phone"/></svg>0171 386 42 19</li>
    <li><svg><use href="#icon-mail"/></svg>info@varnel-immobilien.de</li>
    <li><svg><use href="#icon-web"/></svg>www.varnel-immobilien.de</li>
  </ul>
</section>
</body>
</html>
```